Lena Ashcombe Web

Lena Ashcombe is a singer/songwriter that has a presence in the market for over 20 years. She currently has a website, lenaashcombe.example that needs a major makeover. IT needs to be reorganized to; 1) make it more user friendly; 2) enable multi-languages including; Spanish, French, Russian, Japanese, Chinese and Portuguese; 3) enable purchases online through a storefront of promotional merchandise and music tracks. She has a logo that needs an update, as well as we currently have a business card open on ArtHive for input. Working to re-brand, or refresh her brand.

Lena Ashcombe is the next Rosa Delmont! She has 5 platinum records, Lumen Award nominations and tours with Walter Benning globally and is Nora Quaid's key backup singer for 12 years.
Updates

Some common questions have come up.  Here is some further input:

1) Colors - No specific color in mind but probably earth tones.  Although at this point we''re completely open.  Lena likes classical style, Russian, French decor.  Paris architecture. Greek, Italian textures, Goddess like symbols from the Roman Empire, or the symbols and pomp of the British monarchy.  One name on tap for the new CD is "Silver on the Tide"
2) Halden website - I have not found a new one specifically, but what I don''t like about the existing one is it is not easy to navigate.  Needs to be streamlined and easy to navigate with a storefront for merchandise and music downloads.  
3) On Logo - We''re revamping a "Global" merchandise rollout logo.  We''ve also considered possibly modifying the old english "Ashcombe" family crest which signifies royalty, but have not explored that too much.  The hexagon yellow logo on her current website, I was thinking of modifying to gold (brushed - or polished?), then taking the LA lettering using a fountain pen type look there the line thickness flows with pressure on the pen, then make the gold look like a pillow, with the letter making an impression into the gold pillow.  This expands to a high quality pin, blinged up broach with diamonds imbedded for example, Global label identity, tee shirts, label tag on fashion clothing etc etc. 
 4) One thing marketing has asked us to build is a routine video blog to reach out to fans in a personal way.  Short clips of daily activity, travel prep for shows, etc. Possibly a signup/fanpage where people get emails sent back whenever anything new is posted, like a video blog, new pics, new events.  A menu to choose what you get updates on. 

Thanks, Harold

Target Market(s)

1) Fan base in Europe, Asia, Latin America and North America
2) Movie producers seeking soundtracks
3) Private clients seeking an outstanding performer for corporate events

Industry/Entity Type

Singer

Requirements
Must have
• Better organization into smaller pages. Items critical include: 1) music tracks, 2) Vidstream links, 3) photos & Video, 4) storefront to enable online merchandise purchase 5) a way to illustrate her genre from; gospel, to rock, funk, R&B, country,

```html
<!DOCTYPE html>
<html lang="en">
<head>
<meta charset="utf-8">
<title>Lena Ashcombe</title>
<link href="https://fonts.googleapis.com/css2?family=Oswald:wght@400;500&family=Open+Sans:wght@400;600;700&display=swap" rel="stylesheet">
<style>
  :root{
    --navy:#0a0f1f;
    --navy-bar:#141a30;
    --gold:#f5cf1a;
    --white:#ffffff;
    --light:#ececec;
    --paper:#ffffff;
    --ink:#1d2230;
    --muted:#5a5f6a;
    --frame:#dcdcdc;
  }
  *{box-sizing:border-box;margin:0;padding:0}
  html,body{width:1200px;height:2203px;overflow:hidden}
  body{position:relative;background:var(--navy);font-family:"Open Sans",Arial,sans-serif;color:var(--white)}
  .abs{position:absolute}
  .sky{left:0;top:0;width:1200px;height:405px;background:linear-gradient(180deg,#4f86bd 0%,#8bb0d2 45%,#c9a27a 80%,#8a6a55 100%)}
  .nav{left:122px;top:66px;width:958px;height:66px;background:var(--navy-bar);border-radius:4px 4px 0 0}
  .logo{left:150px;top:72px;width:90px;height:54px;font-family:"Oswald",sans-serif;font-size:40px;font-weight:500;color:var(--gold);line-height:54px;text-align:center}
  .nav-link{top:87px;font-family:"Oswald",sans-serif;font-size:20px;color:var(--white);transform:translateX(-50%);white-space:nowrap;letter-spacing:.2px}
  .nav-link.active{color:var(--gold)}
  .hero{left:122px;top:132px;width:958px;height:348px;background:linear-gradient(135deg,#3a3028 0%,#8a5a2e 35%,#c98a45 55%,#3b2a20 100%)}
  .hero-mark{left:965px;top:380px;font-family:"Oswald",sans-serif;font-size:30px;font-weight:500;color:var(--gold)}
  .player{left:389px;top:347px;width:420px;height:97px;background:rgba(12,14,22,.92);border-radius:4px}
  .player-art{left:8px;top:8px;width:56px;height:56px;background:linear-gradient(135deg,#2a2a2a,#777)}
  .player-title{left:76px;top:7px;font-size:13px;color:#fff}
  .player-title b{color:var(--gold);font-weight:400}
  .player-sub{left:76px;top:25px;font-size:9px;color:#7a7f8c}
  .player-time{left:76px;top:50px;font-size:9px;color:#ccc}
  .player-track{left:133px;top:53px;width:275px;height:7px;background:#2a2d36}
  .player-fill{left:133px;top:53px;width:90px;height:7px;background:var(--gold)}
  .player-bar{left:0;top:72px;width:420px;height:25px;border-top:1px solid #222}
  .dots{left:567px;top:458px;display:flex;gap:3px}
  .dots i{width:12px;height:12px;border:2px solid #fff;border-radius:50%;display:block}
  .h2{font-family:"Oswald",sans-serif;font-size:19px;font-weight:400;text-transform:uppercase}
  .video-card{width:219px}
  .video-thumb{width:219px;height:130px;position:relative}
  .play{position:absolute;left:87px;top:42px;width:46px;height:46px}
  .video-info{position:relative;margin-top:20px;height:40px}
  .video-title{font-size:12px;font-weight:700;color:var(--gold)}
  .video-sub{font-size:10px;line-height:15px;color:#fff}
  .vs{position:absolute;right:0;top:6px;font-size:10px;font-weight:700;color:#fff}
  .gallery{left:0;top:987px;width:1200px;height:445px;background:var(--paper)}
  .g-main{left:129px;top:1049px;width:461px;height:354px;border:6px solid var(--light);background:linear-gradient(160deg,#2a2a2a,#777 50%,#1a1a1a)}
  .g-thumb{width:141px;height:108px;border:6px solid var(--light)}
  .merch{left:0;top:1432px;width:1200px;height:413px;background:var(--light);color:var(--ink)}
  .m-card{top:1503px;width:220px}
  .m-img{width:220px;height:138px;box-shadow:0 2px 4px rgba(0,0,0,.3)}
  .m-title{margin-top:28px;font-family:"Oswald",sans-serif;font-size:14px;color:var(--ink)}
  .m-desc{margin-top:6px;font-size:9.5px;line-height:20px;color:var(--muted);text-align:justify}
  .m-price{margin-top:6px;font-family:"Oswald",sans-serif;font-size:26px;color:var(--ink)}
  .m-btn{margin-top:6px;width:82px;height:31px;background:var(--gold);font-family:"Oswald",sans-serif;font-size:13px;color:var(--ink);text-align:center;line-height:31px;box-shadow:0 2px 0 #b89800}
  .f-head{top:1880px;font-family:"Oswald",sans-serif;font-size:15px;color:var(--gold)}
  .f-list{top:1920px;list-style:none;font-size:12px;line-height:24px}
  .f-input{left:441px;width:220px;height:29px;background:#fff;border-radius:3px;font-size:10px;color:#aaa;padding:8px 8px}
  .submit{left:441px;top:2068px;width:63px;height:21px;background:var(--gold);color:var(--ink);font-family:"Oswald",sans-serif;font-size:11px;text-align:center;line-height:21px}
  .fan{left:671px;top:1865px;width:219px;height:262px;background:#f2f2f2;border:4px solid #d0d0d0;color:#333}
  .fan-name{left:60px;top:14px;font-size:11px;font-weight:700;color:#3b5289}
  .fan-logo{left:10px;top:12px;font-family:"Oswald",sans-serif;font-size:24px;color:var(--gold)}
  .fan-like{left:60px;top:32px;width:38px;height:14px;background:#4a63a0;color:#fff;font-size:8px;text-align:center;line-height:14px}
  .fan-count{left:10px;top:80px;font-size:8px;color:#444}
  .fan-grid{left:10px;top:100px;display:grid;grid-template-columns:repeat(4,44px);gap:4px}
  .fan-grid i{display:block;width:44px;height:40px;background:linear-gradient(135deg,#5a4030,#b08a6a)}
  .soc{left:931px;font-size:12px}
  .soc-icon{left:1024px;width:18px;height:18px;border-radius:50%;background:#fff}
  .copyright{left:0;top:2163px;width:1200px;text-align:center;font-size:11px;color:#ddd}
</style>
</head>
<body>

<div class="abs sky" role="img" aria-label="Paris rooftops under a blue evening sky"></div>

<header>
  <div class="abs nav"></div>
  <div class="abs logo">LA</div>
  <nav>
    <span class="abs nav-link active" style="left:301px">HOME</span>
    <span class="abs nav-link" style="left:392px">EVENTS</span>
    <span class="abs nav-link" style="left:486px">MUSIC</span>
    <span class="abs nav-link" style="left:573px">VIDEO</span>
    <span class="abs nav-link" style="left:671px">PICTURES</span>
    <span class="abs nav-link" style="left:774px">ABOUT</span>
    <span class="abs nav-link" style="left:890px">DISCOGRAPHY</span>
    <span class="abs nav-link" style="left:1018px">CONTACT</span>
  </nav>
</header>

<section class="abs hero" role="img" aria-label="Portrait of the singer seated in a car with tan leather seats"></section>
<div class="abs hero-mark">LA</div>

<div class="abs player">
  <div class="abs player-art" role="img" aria-label="Album cover art"></div>
  <div class="abs player-title"><b>Halden</b> - Turned the Way You Hold Me</div>
  <div class="abs player-sub">Lights Over Water</div>
  <div class="abs player-time">0:46 / 3:12</div>
  <div class="abs player-track"></div>
  <div class="abs player-fill"></div>
  <div class="abs player-bar">
    <svg width="420" height="25" viewBox="0 0 420 25">
      <polygon points="12,8 12,17 19,12.5" fill="#fff"/>
      <polygon points="42,12.5 47,9 47,16" fill="#fff"/><polygon points="37,12.5 42,9 42,16" fill="#fff"/>
      <polygon points="76,9 81,12.5 76,16" fill="#fff"/><polygon points="81,9 86,12.5 81,16" fill="#fff"/>
      <polygon points="318,10 321,10 325,7 325,18 321,15 318,15" fill="#aaa"/>
      <rect x="333" y="11.5" width="60" height="2" fill="#777"/>
      <rect x="333" y="11.5" width="45" height="2" fill="#fff"/>
      <circle cx="378" cy="12.5" r="3.5" fill="#fff"/>
    </svg>
  </div>
</div>
<div class="abs dots"><i></i><i></i><i></i><i></i></div>

<section>
  <h2 class="abs h2" style="left:131px;top:508px">Videos</h2>

  <div class="abs video-card" style="left:131px;top:546px">
    <div class="video-thumb" role="img" aria-label="Video still of the singer in a yellow hood" style="background:linear-gradient(135deg,#111,#8a7420 60%,#111)">
      <svg class="play" viewBox="0 0 46 46"><circle cx="23" cy="23" r="21" fill="#fff" fill-opacity=".9"/><polygon points="18,13 18,33 33,23" fill="#111"/></svg>
    </div>
    <div class="video-info"><div class="video-title">Walter Benning's</div><div class="video-sub">Groovelight Parade Thang<br>ft. Lena Ashcombe</div><span class="vs">Vidstream</span></div>
  </div>
  <div class="abs video-card" style="left:370px;top:546px">
    <div class="video-thumb" role="img" aria-label="Video still of a band performing on a warm-lit stage" style="background:linear-gradient(135deg,#2a1a10,#8a5230 55%,#1a100a)">
      <svg class="play" viewBox="0 0 46 46"><circle cx="23" cy="23" r="21" fill="#fff" fill-opacity=".9"/><polygon points="18,13 18,33 33,23" fill="#111"/></svg>
    </div>
    <div class="video-info"><div class="video-title">Walter Benning's</div><div class="video-sub">Groovelight Parade Thang<br>ft. Lena Ashcombe</div><span class="vs">Vidstream</span></div>
  </div>
  <div class="abs video-card" style="left:610px;top:546px">
    <div class="video-thumb" role="img" aria-label="Video still of a concert stage under blue lights" style="background:linear-gradient(160deg,#1a3aa0,#3a6ad0 50%,#0a1a50)">
      <svg class="play" viewBox="0 0 46 46"><circle cx="23" cy="23" r="21" fill="#fff" fill-opacity=".9"/><polygon points="18,13 18,33 33,23" fill="#111"/></svg>
    </div>
    <div class="video-info"><div class="video-title">Walter Benning's</div><div class="video-sub">Groovelight Parade Thang<br>ft. Lena Ashcombe</div><span class="vs">Vidstream</span></div>
  </div>
  <div class="abs video-card" style="left:849px;top:546px">
    <div class="video-thumb" role="img" aria-label="Video still of a dim stage with dark curtains" style="background:linear-gradient(135deg,#1a0a0a,#4a2020 50%,#0a0505)">
      <svg class="play" viewBox="0 0 46 46"><circle cx="23" cy="23" r="21" fill="#fff" fill-opacity=".9"/><polygon points="18,13 18,33 33,23" fill="#111"/></svg>
    </div>
    <div class="video-info"><div class="video-title">Walter Benning's</div><div class="video-sub">Groovelight Parade Thang<br>ft. Lena Ashcombe</div><span class="vs">Vidstream</span></div>
  </div>

  <div class="abs video-card" style="left:131px;top:768px">
    <div class="video-thumb" role="img" aria-label="Black and white video still of the singer at a microphone" style="background:linear-gradient(135deg,#222,#999 55%,#333)">
      <svg class="play" viewBox="0 0 46 46"><circle cx="23" cy="23" r="21" fill="#fff" fill-opacity=".9"/><polygon points="18,13 18,33 33,23" fill="#111"/></svg>
    </div>
    <div class="video-info"><div class="video-title">Walter Benning's</div><div class="video-sub">Groovelight Parade Thang<br>ft. Lena Ashcombe</div><span class="vs">Vidstream</span></div>
  </div>
  <div class="abs video-card" style="left:370px;top:768px">
    <div class="video-thumb" role="img" aria-label="Video still of singers on a pink-lit stage" style="background:linear-gradient(135deg,#5a1040,#d04a90 55%,#3a0a2a)">
      <svg class="play" viewBox="0 0 46 46"><circle cx="23" cy="23" r="21" fill="#fff" fill-opacity=".9"/><polygon points="18,13 18,33 33,23" fill="#111"/></svg>
    </div>
    <div class="video-info"><div class="video-title">Walter Benning's</div><div class="video-sub">Groovelight Parade Thang<br>ft. Lena Ashcombe</div><span class="vs">Vidstream</span></div>
  </div>
  <div class="abs video-card" style="left:610px;top:768px">
    <div class="video-thumb" role="img" aria-label="Video still of a performer under golden stage light" style="background:linear-gradient(135deg,#2a200a,#9a8040 55%,#1a1408)">
      <svg class="play" viewBox="0 0 46 46"><circle cx="23" cy="23" r="21" fill="#fff" fill-opacity=".9"/><polygon points="18,13 18,33 33,23" fill="#111"/></svg>
    </div>
    <div class="video-info"><div class="video-title">Walter Benning's</div><div class="video-sub">Groovelight Parade Thang<br>ft. Lena Ashcombe</div><span class="vs">Vidstream</span></div>
  </div>
  <div class="abs video-card" style="left:849px;top:768px">
    <div class="video-thumb" role="img" aria-label="Video still of the singer under red and blue lights" style="background:linear-gradient(135deg,#c02040,#6a3ab0 55%,#2040a0)">
      <svg class="play" viewBox="0 0 46 46"><circle cx="23" cy="23" r="21" fill="#fff" fill-opacity=".9"/><polygon points="18,13 18,33 33,23" fill="#111"/></svg>
    </div>
    <div class="video-info"><div class="video-title">Walter Benning's</div><div class="video-sub">Groovelight Parade Thang<br>ft. Lena Ashcombe</div><span class="vs">Vidstream</span></div>
  </div>
</section>

<section class="abs gallery"></section>
<h2 class="abs h2" style="left:129px;top:1011px;color:var(--ink)">Picture Gallery</h2>
<div class="abs g-main" role="img" aria-label="Black and white photo of the singer on stage">
  <svg class="abs" style="left:12px;top:146px" width="30" height="50" viewBox="0 0 30 50"><polyline points="24,4 6,25 24,46" fill="none" stroke="#fff" stroke-width="5"/></svg>
  <svg class="abs" style="right:12px;top:146px" width="30" height="50" viewBox="0 0 30 50"><polyline points="6,4 24,25 6,46" fill="none" stroke="#fff" stroke-width="5"/></svg>
</div>
<div class="abs g-thumb" style="left:608px;top:1049px;background:linear-gradient(135deg,#3a2010,#a06040)" role="img" aria-label="Photo of the singer performing"></div>
<div class="abs g-thumb" style="left:770px;top:1049px;background:linear-gradient(135deg,#3a1020,#c03060)" role="img" aria-label="Photo of the singer with a guitarist"></div>
<div class="abs g-thumb" style="left:931px;top:1049px;background:linear-gradient(135deg,#4a2a30,#b07a70)" role="img" aria-label="Photo of the singer with a fellow performer"></div>
<div class="abs g-thumb" style="left:608px;top:1171px;background:linear-gradient(135deg,#5a4030,#c0503a)" role="img" aria-label="Photo of the singer in a red dress"></div>
<div class="abs g-thumb" style="left:770px;top:1171px;background:linear-gradient(135deg,#6a7a5a,#c0a080)" role="img" aria-label="Photo of the singer outdoors with fans"></div>
<div class="abs g-thumb" style="left:931px;top:1171px;background:linear-gradient(135deg,#2a1a1a,#7a5a50)" role="img" aria-label="Photo of an embrace backstage"></div>
<div class="abs g-thumb" style="left:608px;top:1291px;background:linear-gradient(135deg,#8a6a50,#d0b090)" role="img" aria-label="Portrait photo of the singer smiling"></div>
<div class="abs g-thumb" style="left:770px;top:1291px;background:linear-gradient(135deg,#e8e8e8,#b0a090)" role="img" aria-label="Photo of the singer in a white outfit"></div>
<div class="abs g-thumb" style="left:931px;top:1291px;background:linear-gradient(135deg,#6a3010,#d07030)" role="img" aria-label="Photo of the singer by a window in warm light"></div>

<section class="abs merch"></section>
<h2 class="abs h2" style="left:128px;top:1454px;color:var(--ink)">Purchase Merchandise</h2>
<svg class="abs" style="left:1026px;top:1456px" width="44" height="22" viewBox="0 0 44 22"><polyline points="12,3 4,11 12,19" fill="none" stroke="#1d2230" stroke-width="3"/><polyline points="32,3 40,11 32,19" fill="none" stroke="#1d2230" stroke-width="3"/></svg>

<div class="abs m-card" style="left:128px">
  <div class="m-img" role="img" aria-label="Framed photo of the singer with a group at a formal event" style="background:linear-gradient(135deg,#3a3a60,#b08070 50%,#2a2a3a)"></div>
  <div class="m-title">LENA ASHCOMBE - PHOTO FRAMES</div>
  <div class="m-desc">Lorem Ipsum is simply dummy text of the printing and typesetting industry.</div>
  <div class="m-price">$59.00</div>
  <div class="m-btn">ADD CART</div>
</div>
<div class="abs m-card" style="left:369px">
  <div class="m-img" role="img" aria-label="Framed photo of the singer against a blue backdrop" style="background:linear-gradient(135deg,#0a2a8a,#3a8ae0 50%,#0a1a50)"></div>
  <div class="m-title">LENA ASHCOMBE - PHOTO FRAMES</div>
  <div class="m-desc">Lorem Ipsum is simply dummy text of the printing and typesetting industry.</div>
  <div class="m-price">$59.00</div>
  <div class="m-btn">ADD CART</div>
</div>
<div class="abs m-card" style="left:609px">
  <div class="m-img" role="img" aria-label="Framed photo of the singer in a yellow coat" style="background:linear-gradient(135deg,#4a2a6a,#c0a040 55%,#2a1a3a)"></div>
  <div class="m-title">LENA ASHCOMBE - PHOTO FRAMES</div>
  <div class="m-desc">Lorem Ipsum is simply dummy text of the printing and typesetting industry.</div>
  <div class="m-price">$59.00</div>
  <div class="m-btn">ADD CART</div>
</div>
<div class="abs m-card" style="left:849px">
  <div class="m-img" role="img" aria-label="Framed photo of the singer performing under stage light" style="background:linear-gradient(135deg,#2a1008,#c06030 50%,#1a0a05)"></div>
  <div class="m-title">LENA ASHCOMBE - PHOTO FRAMES</div>
  <div class="m-desc">Lorem Ipsum is simply dummy text of the printing and typesetting industry.</div>
  <div class="m-price">$59.00</div>
  <div class="m-btn">ADD CART</div>
</div>

<footer>
  <div class="abs f-head" style="left:129px">MENU LINKS</div>
  <ul class="abs f-list" style="left:129px">
    <li>Home</li><li>Events</li><li>Music</li><li>Video</li><li>Pictures</li><li>About</li><li>Discography</li><li>Contact</li>
  </ul>
  <div class="abs f-head" style="left:269px">OTHER LINKS</div>
  <ul class="abs f-list" style="left:269px">
    <li>Terms &amp; Conditions</li><li>Privacy Policy</li><li>Legal Notice</li><li>Disclaimer</li>
  </ul>
  <div class="abs f-head" style="left:441px">LENA ASHCOMBE NEWSLETTER</div>
  <div class="abs f-input" style="top:1915px">Name</div>
  <div class="abs f-input" style="top:1952px">Last E-Mail</div>
  <div class="abs f-input" style="top:1989px">E-Mail</div>
  <div class="abs f-input" style="top:2025px">I'm
    <svg class="abs" style="right:8px;top:8px" width="14" height="14" viewBox="0 0 14 14"><rect x=".5" y=".5" width="13" height="13" fill="none" stroke="#999"/><polygon points="4,5 10,5 7,9" fill="#555"/></svg>
  </div>
  <div class="abs submit">SUBMIT</div>

  <div class="abs fan">
    <div class="abs fan-logo">LA</div>
    <div class="abs fan-name">Lena Ashcombe Fanpage</div>
    <div class="abs fan-like">Like</div>
    <div class="abs fan-count">2,314 people like Lena Ashcombe Fanpage.</div>
    <div class="abs fan-grid" role="img" aria-label="Grid of fan profile photos"><i></i><i></i><i></i><i></i><i></i><i></i><i></i><i></i><i></i><i></i><i></i><i></i><i></i><i></i><i></i><i></i></div>
  </div>

  <div class="abs f-head" style="left:931px">LINKS</div>
  <div class="abs soc" style="top:1922px">Facepage</div><div class="abs soc-icon" style="top:1922px"></div>
  <div class="abs soc" style="top:1961px">Chirper</div><div class="abs soc-icon" style="top:1961px"></div>
  <div class="abs soc" style="top:2001px">Vidstream</div><div class="abs soc-icon" style="top:2001px"></div>
  <div class="abs soc" style="top:2041px">RSS Feed</div><div class="abs soc-icon" style="top:2041px"></div>

  <div class="abs copyright">Copyright ©2013 Company Name &nbsp; - All rights reserved</div>
</footer>

</body>
</html>
```